Velarine Retractable Banner

I need a banner designed to advertise my skincare brand at a meeting. I want it to be eye-catching, yet elegant and modern and it should keep with my branding from my website (www.velarine-example.com). Please let me know if you need any addition files or photos.

I have included the specs for the size I plan to order.

```html
<!DOCTYPE html>
<html lang="en">
<head>
<meta charset="utf-8">
<title>Velarine Retractable Banner</title>
<link rel="stylesheet" href="https://fonts.googleapis.com/css2?family=Abril+Fatface&family=Cinzel:wght@400&family=Montserrat:wght@400;700&display=swap">
<style>
  :root {
    --backdrop: #e9c1ae;
    --bronze: #9a5a2c;
    --bronze-light: #c98a58;
    --bronze-dark: #7e4620;
    --blush: #f3cfc1;
    --cream: #fdf3ee;
    --ink: #5a3a2a;
    --white: #ffffff;
  }
  * { margin: 0; padding: 0; box-sizing: border-box; }
  html, body { width: 818px; height: 1200px; overflow: hidden; }
  body { background: var(--backdrop); font-family: "Montserrat", sans-serif; }

  .banner {
    position: absolute; left: 169px; top: 12px;
    width: 480px; height: 1176px; overflow: hidden;
    background: linear-gradient(180deg, var(--white) 0%, var(--white) 60%, var(--cream) 80%, #fbe4da 100%);
    box-shadow: 0 10px 30px rgba(120, 70, 40, 0.18);
  }
  .banner-shapes { position: absolute; inset: 0; }

  .brand-header {
    position: absolute; left: 0; top: 0; width: 480px; height: 142px;
    background: linear-gradient(180deg, var(--white) 0%, #fbeae2 100%);
    text-align: center;
  }
  .brand-name {
    font-family: "Abril Fatface", serif; font-weight: 400;
    font-size: 62px; line-height: 1; color: var(--bronze);
    padding-top: 30px; letter-spacing: -0.5px;
  }
  .brand-byline {
    font-size: 19px; color: var(--bronze); margin-top: 4px; letter-spacing: 0.5px;
  }

  .headline {
    position: absolute; left: 236px; top: 458px; width: 200px;
    font-family: "Abril Fatface", serif; font-weight: 400;
    font-size: 58px; line-height: 0.82; color: var(--bronze); text-align: right;
  }
  .headline span { display: block; }

  .product-shot {
    position: absolute; left: 78px; top: 505px; width: 303px; height: 290px;
    background: radial-gradient(ellipse at 45% 60%, #ffffff 0%, #f6f0ec 65%, #efe5df 100%);
    clip-path: polygon(0 0, 50% 0, 50% 58%, 100% 58%, 100% 100%, 0 100%);
  }

  .intro {
    position: absolute; left: 30px; top: 828px; width: 420px;
    font-size: 14.3px; line-height: 1.25; color: var(--ink); text-align: center;
  }

  .results-title {
    position: absolute; left: 33px; top: 920px;
    font-family: "Cinzel", serif; font-weight: 400; font-size: 34px; line-height: 1.02; color: var(--bronze);
  }

  .cta {
    position: absolute; left: 30px;
    background: linear-gradient(90deg, var(--bronze-dark) 0%, var(--bronze-light) 50%, var(--bronze) 100%);
    color: var(--white); font-weight: 700; white-space: nowrap;
  }
  .cta-shop { top: 1009px; height: 35px; padding: 0 16px; font-size: 20px; line-height: 35px; display: flex; align-items: center; gap: 14px; }
  .cta-url { top: 1053px; height: 37px; padding: 0 16px; font-size: 16px; line-height: 37px; }

  .contact {
    position: absolute; left: 0; top: 1113px; width: 480px;
    display: flex; justify-content: center; align-items: center; gap: 10px;
    font-size: 17px; color: var(--ink);
  }
</style>
</head>
<body>
  <main class="banner">
    <svg class="banner-shapes" width="480" height="1176" viewBox="0 0 480 1176">
      <defs>
        <linearGradient id="photo-tones" x1="0" y1="0" x2="1" y2="1">
          <stop offset="0" stop-color="#c9a08c"/>
          <stop offset="0.45" stop-color="#b7674a"/>
          <stop offset="0.75" stop-color="#e8cfc3"/>
          <stop offset="1" stop-color="#9fb6c6"/>
        </linearGradient>
        <linearGradient id="portrait-tones" x1="0" y1="0" x2="1" y2="1">
          <stop offset="0" stop-color="#d9b7a6"/>
          <stop offset="0.5" stop-color="#f1e6e0"/>
          <stop offset="1" stop-color="#e3b9a3"/>
        </linearGradient>
      </defs>
      <rect class="hero-photo" role="img" aria-label="Photo of a red-haired woman applying skincare while looking in a mirror" x="0" y="142" width="480" height="300" fill="url(#photo-tones)"/>
      <path class="heart-panel" d="M0,375 C50,340 190,335 238,437 C286,335 430,340 480,375 L480,760 Q380,830 238,860 Q100,830 0,760 Z" fill="#ffffff"/>
      <g class="accent-hearts" fill="var(--blush)">
        <path d="M123,470 C108,458 96,448 100,434 C104,420 122,420 126,432 C130,418 150,418 152,432 C155,448 138,460 123,470 Z"/>
        <path d="M174,489 C167,484 161,479 163,473 C165,467 173,467 175,472 C177,466 186,466 187,473 C188,480 181,484 174,489 Z"/>
      </g>
      <path class="results-photo" role="img" aria-label="Photo of a woman holding a serum bottle near her face, framed in a heart" d="M318,1048 C290,1020 268,990 270,950 C272,910 310,893 340,912 C360,870 420,880 446,912 C470,945 455,985 420,1010 C390,1030 355,1040 318,1048 Z" fill="url(#portrait-tones)" stroke="#ffffff" stroke-width="6"/>
    </svg>

    <header class="brand-header">
      <h1 class="brand-name">Velarine</h1>
      <p class="brand-byline">by dr. elena marsh</p>
    </header>

    <div class="product-shot" role="img" aria-label="Product photo of a cream bottle, serum dropper bottle and exfoliator jar"></div>

    <h2 class="headline"><span>Made</span><span>for</span><span>your</span><span>glow</span></h2>

    <p class="intro">Patented, medical grade skincare backed by Dr. Elena Marsh’s revolutionary scientific discovery. Made with only the best ingredients for your skin.</p>

    <h3 class="results-title">IMPRESSIVE<br>RESULTS</h3>

    <div class="cta cta-shop">Shop Today
      <svg width="26" height="16" viewBox="0 0 26 16" aria-hidden="true"><path d="M1 8 H24 M17 1 L24 8 L17 15" fill="none" stroke="#fff" stroke-width="1.8"/></svg>
    </div>
    <div class="cta cta-url">www.velarine-example.com</div>

    <footer class="contact">
      <span>555.014.2290</span>
      <svg width="20" height="17" viewBox="0 0 20 17" aria-hidden="true"><path d="M10 17 C4 12 0 9 1 5 C2 0 8 0 10 4 C12 0 18 0 19 5 C20 9 16 12 10 17 Z" fill="var(--blush)"/></svg>
      <span>info@velarine-example.com</span>
    </footer>
  </main>
</body>
</html>
```